Flyer-Design / Verodina
Zielgruppe
Licht zu verstehen und richtig einzusetzen ist ein wesentlicher Bestandteil, um die Wirkung von Architektur, Innenräumen und Landschaften zu unterstützen und zu steigern. Die harmonische Verschmelzung von moderner Architektur und akzentuiert eingesetztem Licht verleiht Innenräumen ihre eigene Note. Dieses Zusammenspiel erfordert über das Berechnen und die Leuchtenauswahl hinaus einen sehr sensiblen Umgang mit dem Medium Licht. Bei jeder Lichtplanung steht der Mensch mit seiner Wahrnehmung von Licht und Schatten im Mittelpunkt. Eine hochwertige Lichtplanung vom Fachmann verfolgt mit ihrem ganzheitlichen Ansatz daher den Anspruch Atmosphäre, Wohlbefinden und Orientierung zu schaffen und den beleuchteten Räumen Ausdruckskraft zu verleihen.
Aufgabenstellung
WIr möchten einen Flyer für unseren Laden der für den Kunden sehr ansprechend ist, im Bezug auf unserer Planungen und unseren Handel.
Wir möchten darauf eine Zusammenfassung unser Arbeit und unserer Portfolios sehen die dem Kunden sofort sagen was wir machen.

```html
<!DOCTYPE html>
<html lang="de">
<head>
<meta charset="utf-8">
<title>Verodina – Flyer</title>
<link href="https://fonts.googleapis.com/css2?family=Inter:wght@300;400&family=Didact+Gothic&display=swap" rel="stylesheet">
<style>
  :root{
    --dark:#2f3336;
    --yellow:#ffe500;
    --ink:#2b2b2b;
    --paper:#ffffff;
    --muted:#9a9ea1;
  }
  *{margin:0;padding:0;box-sizing:border-box}
  html,body{width:1200px;height:1200px;overflow:hidden;background:var(--paper)}
  body{position:relative;font-family:"Inter",Arial,sans-serif;color:var(--ink)}

  .sheet{position:absolute;background:var(--dark);overflow:hidden;box-shadow:2px 3px 5px rgba(0,0,0,.35)}
  .sheet-outside{left:28px;top:23px;width:678px;height:479px}
  .sheet-title{left:727px;top:23px;width:224px;height:479px}
  .sheet-back{left:971px;top:23px;width:224px;height:479px}
  .sheet-inside{left:28px;top:594px;width:678px;height:479px;box-shadow:none}
  .sheet-open{left:755px;top:606px;width:406px;height:467px}

  .view-label{position:absolute;font-family:"Didact Gothic",Arial,sans-serif;font-size:25px;color:#222;letter-spacing:.5px}

  .disc{position:absolute;border-radius:50%;background:var(--yellow)}

  .text-panel{position:absolute;background:var(--paper);overflow:hidden}
  .text-panel .headline{color:var(--yellow);font-weight:400;font-size:15px;position:absolute}
  .text-panel .body-copy{position:absolute;font-size:7.6px;line-height:1.27;color:#333}
  .text-panel .body-copy p{margin-bottom:9.5px}
  .claim-find{position:absolute;font-weight:300;font-size:26px;line-height:31px;color:var(--ink)}

  .brand{position:absolute;text-align:right}
  .brand-name{font-family:"Inter",Arial,sans-serif;font-weight:300;font-size:26px;letter-spacing:3px;color:var(--paper);line-height:1}
  .brand-tag{position:absolute;font-family:"Didact Gothic",Arial,sans-serif;font-size:7.5px;letter-spacing:1px;color:var(--muted);text-align:left;line-height:1.3;white-space:nowrap}

  .claim-light{position:absolute;font-weight:300;font-size:26px;color:var(--ink);white-space:nowrap;text-align:right}
  .claim-light .gap{display:inline-block;width:16px}

  .contact{position:absolute;text-align:right;font-size:9.8px;line-height:11.6px;color:var(--ink);white-space:nowrap}

  .photo{position:absolute;border-radius:50%;box-shadow:6px 6px 8px rgba(0,0,0,.55)}
  .photo-pendant{background:radial-gradient(circle at 50% 35%,#4a4a4a 0%,#363636 55%,#2a2a2a 100%)}
  .photo-chandelier{background:radial-gradient(circle at 50% 45%,#e4e4e4 0%,#fafafa 45%,#ffffff 100%)}
  .photo-wall{background:radial-gradient(circle at 50% 50%,#3a3f48 0%,#3a3f48 28%,#c9c9c9 30%,#9d9d9d 70%,#7a7a7a 100%)}
  .photo-gold{background:radial-gradient(ellipse at 50% 55%,#3b2c12 0%,#2a2a2a 30%,#d8d8d8 34%,#e7e7e7 60%,#cfcfcf 100%)}

  .bubble{position:absolute;border-radius:50%;background:var(--yellow);display:flex;align-items:center;padding-left:18px;font-size:8.8px;line-height:10.2px;color:#3a3a2a}
</style>
</head>
<body>

<!-- Outside spread -->
<section class="sheet sheet-outside" aria-label="Außenseite">
  <div class="disc" style="left:278px;top:233px;width:348px;height:348px"></div>

  <div class="text-panel" style="left:12px;top:11px;width:214px;height:468px">
    <h2 class="headline" style="left:7px;top:12px">Headline Headline</h2>
    <div class="body-copy" style="left:7px;top:73px;width:200px">
      <p>Lorem ipsum dolor sit amet, consectetuer adipiscing elit. Aenean commodo ligula eget dolor. Aenean massa. Cum sociis natoque penatibus et magnis dis parturient montes, nascetur ridiculus mus. Donec quam felis, ultricies nec, pellentesque eu, pretium quis, sem.</p>
      <p>Nulla consequat massa quis enim. Donec pede justo, fringilla vel, aliquet nec, vulputate eget, arcu. In enim justo, rhoncus ut, imperdiet a, venenatis vitae, justo. Nullam dictum felis eu pede mollis pretium. Integer tincidunt. Cras dapibus. Vivamus elementum semper nisi.</p>
      <p>Aenean vulputate eleifend tellus. Aenean leo ligula, porttitor eu, consequat vitae, eleifend ac, enim. Aliquam lorem ante, dapibus in, viverra quis, feugiat a, tellus. Phasellus viverra nulla ut metus varius laoreet.</p>
      <p>Quisque rutrum. Aenean imperdiet.</p>
    </div>
  </div>
  <div class="disc" style="left:-1px;top:315px;width:216px;height:216px"></div>
  <p class="claim-find" style="left:20px;top:380px">bei uns finden<br>Sie die richtige<br>Leuchte</p>

  <div class="contact" style="right:237px;top:366px">
    Verodina<br>Lindenhofweg 12<br>91700 Talheim<br>Tel: +49 9800-1234567<br>Email: info@verodina.de<br>www.verodina.de<br><br>Öffnungszeiten:<br>(Mo–Fr.) 8:00–17:00
  </div>

  <div class="brand" style="right:17px;top:58px">
    <div class="brand-name">VERODINA</div>
  </div>
  <div class="brand-tag" style="left:555px;top:89px">Lichtberatung +<br>Fachhandel</div>

  <p class="claim-light" style="right:17px;top:306px">wir machen<span class="gap"></span>licht</p>
</section>
<span class="view-label" style="left:50px;top:510px">aussen</span>

<!-- Title panel -->
<section class="sheet sheet-title" aria-label="Titelseite">
  <div class="disc" style="left:-175px;top:233px;width:348px;height:348px"></div>
  <div class="brand" style="right:17px;top:58px">
    <div class="brand-name">VERODINA</div>
  </div>
  <div class="brand-tag" style="left:101px;top:89px">Lichtberatung +<br>Fachhandel</div>
  <p class="claim-light" style="right:16px;top:306px">wir machen<span class="gap"></span>licht</p>
</section>
<span class="view-label" style="left:734px;top:510px">Titel</span>

<!-- Back panel -->
<section class="sheet sheet-back" aria-label="Rückseite">
  <div class="disc" style="left:52px;top:233px;width:348px;height:348px"></div>
  <div class="contact" style="right:9px;top:366px">
    Verodina<br>Lindenhofweg 12<br>91700 Talheim<br>Tel: +49 9800-1234567<br>Email: info@verodina.de<br>www.verodina.de<br><br>Öffnungszeiten:<br>(Mo–Fr.) 8:00–17:00
  </div>
</section>
<span class="view-label" style="left:977px;top:501px">Rückseite</span>

<!-- Inside spread -->
<section class="sheet sheet-inside" aria-label="Innenseite">
  <div class="photo photo-pendant" style="left:-42px;top:-21px;width:190px;height:190px" role="img" aria-label="Foto: schwarze Pendelleuchte über einem Sideboard"></div>
  <div class="photo photo-chandelier" style="left:243px;top:-2px;width:190px;height:190px" role="img" aria-label="Foto: Kristall-Kronleuchter"></div>
  <div class="photo photo-pendant" style="left:443px;top:98px;width:190px;height:190px" role="img" aria-label="Foto: schwarze Pendelleuchte über einem Sideboard"></div>
  <div class="photo photo-wall" style="left:25px;top:269px;width:190px;height:190px" role="img" aria-label="Foto: runde Wandleuchte mit Licht nach oben und unten"></div>
  <div class="photo photo-gold" style="left:272px;top:296px;width:190px;height:190px" role="img" aria-label="Foto: schwarze Wandleuchte mit goldenem Innenring"></div>
  <div class="photo photo-wall" style="left:476px;top:323px;width:190px;height:190px" role="img" aria-label="Foto: runde Wandleuchte mit Licht nach oben und unten"></div>

  <div class="bubble" style="left:118px;top:76px;width:88px;height:88px">Lorem ipsum<br>dolor sit amet,<br>consectetuer<br>adipiscing elit.</div>
  <div class="bubble" style="left:255px;top:155px;width:88px;height:88px">Lorem ipsum<br>dolor sit amet,<br>consectetuer<br>adipiscing elit.</div>
  <div class="bubble" style="left:507px;top:19px;width:88px;height:88px">Lorem ipsum<br>dolor sit amet,<br>consectetuer<br>adipiscing elit.</div>
  <div class="bubble" style="left:19px;top:222px;width:88px;height:88px">Lorem ipsum<br>dolor sit amet,<br>consectetuer<br>adipiscing elit.</div>
  <div class="bubble" style="left:353px;top:254px;width:88px;height:88px">Lorem ipsum<br>dolor sit amet,<br>consectetuer<br>adipiscing elit.</div>
  <div class="bubble" style="left:578px;top:280px;width:88px;height:88px">Lorem ipsum<br>dolor sit amet,<br>consectetuer<br>adipiscing elit.</div>
</section>
<span class="view-label" style="left:39px;top:1088px">innen</span>

<!-- Opened once -->
<section class="sheet sheet-open" aria-label="Einmal aufgeklappt">
  <div class="photo photo-pendant" style="left:-11px;top:-18px;width:162px;height:162px" role="img" aria-label="Foto: schwarze Pendelleuchte über einem Sideboard"></div>
  <div class="photo photo-wall" style="left:23px;top:264px;width:172px;height:172px" role="img" aria-label="Foto: runde Wandleuchte mit Licht nach oben und unten"></div>
  <div class="bubble" style="left:109px;top:84px;width:78px;height:78px;padding-left:16px;font-size:7.6px;line-height:9px">Lorem ipsum<br>dolor sit amet,<br>consectetuer<br>adipiscing elit.</div>
  <div class="bubble" style="left:19px;top:220px;width:78px;height:78px;padding-left:16px;font-size:7.6px;line-height:9px">Lorem ipsum<br>dolor sit amet,<br>consectetuer<br>adipiscing elit.</div>

  <div class="text-panel" style="left:206px;top:19px;width:194px;height:448px">
    <div class="disc" style="left:-2px;top:309px;width:194px;height:194px"></div>
    <h2 class="headline" style="left:8px;top:16px;font-size:13px">Headline Headline</h2>
    <div class="body-copy" style="left:8px;top:66px;width:180px;font-size:6.8px;line-height:1.25">
      <p style="margin-bottom:8px">Lorem ipsum dolor sit amet, consectetuer adipiscing elit. Aenean commodo ligula eget dolor. Aenean massa. Cum sociis natoque penatibus et magnis dis parturient montes, nascetur ridiculus mus. Donec quam felis, ultricies nec, pellentesque eu, pretium quis, sem.</p>
      <p style="margin-bottom:8px">Nulla consequat massa quis enim. Donec pede justo, fringilla vel, aliquet nec, vulputate eget, arcu. In enim justo, rhoncus ut, imperdiet a, venenatis vitae, justo. Nullam dictum felis eu pede mollis pretium. Integer tincidunt. Cras dapibus. Vivamus elementum semper nisi.</p>
      <p style="margin-bottom:8px">Aenean vulputate eleifend tellus. Aenean leo ligula, porttitor eu, consequat vitae, eleifend ac, enim. Aliquam lorem ante, dapibus in, viverra quis, feugiat a, tellus. Phasellus viverra nulla ut metus varius laoreet.</p>
      <p>Quisque rutrum. Aenean imperdiet.</p>
    </div>
    <p class="claim-find" style="left:8px;top:352px;font-size:22px;line-height:27px">bei uns finden<br>Sie die richtige<br>Leuchte</p>
  </div>
</section>
<span class="view-label" style="left:769px;top:1138px">1x aufgeklappt</span>

</body>
</html>
```